Alternative Health business needs a self help book cover design

Pale Brook Healing requires an E book and print cover design for a new self help book titled "Making The Bright Choice". Sub title 'Ways to build the glad days YOU seek' . Author Dorinda Crastley. The book is about deliberately changing things now, so you feel happy now and this then flows out an effects everything else in your life. It combines NLP, yoga philosophy and modern psychology in a down to earth, easy to read manner. I would like the cover to be happy, colourful, beautiful, artistic and hip. Maybe something hand drawn or painted. Something a woman would want to display and something that makes you smile and feel happy.
I don't want it to look like a romance novel and would prefer no photos of people. Pics are of other peoples covers I like. Thank you in advance. dorinda

Target Market(s)

woman 18-50

Industry/Entity Type

Business

Requirements
Must have
• happy feeling. professional look
Nice to have
• original drawing or painting
Should not have
• photos of real people, yellow smiley faces, sunsets, butterflies, yoga, tree, elements of my business logo

```html
<!DOCTYPE html>
<html lang="en">
<head>
<meta charset="utf-8">
<title>Making The Bright Choice — Dorinda Crastley</title>
<link rel="stylesheet" href="https://fonts.googleapis.com/css2?family=Pinyon+Script&family=Libre+Baskerville&family=Lato:wght@400&display=swap">
<style>
  :root {
    --paper: #f1e6cc;
    --paper-warm: #e9d6ae;
    --rust: #a4502a;
    --umber: #6b3a22;
    --ochre: #c98a3c;
    --sienna: #8a4a2c;
    --teal-splash: #3e6f6c;
    --band-gold: #d5ba72;
    --ink: #3c2a1c;
  }
  * { margin: 0; padding: 0; box-sizing: border-box; }
  html, body {
    width: 738px;
    height: 1200px;
    overflow: hidden;
    background: var(--paper);
  }
  .cover {
    position: relative;
    width: 738px;
    height: 1200px;
    background: var(--paper);
    overflow: hidden;
  }
  .cover-art {
    position: absolute;
    left: 0;
    top: 0;
    width: 738px;
    height: 1013px;
    background:
      radial-gradient(ellipse 260px 300px at 330px 520px, #f3e4cc 0%, rgba(243,228,204,0) 70%),
      radial-gradient(ellipse 320px 260px at 300px 300px, var(--ochre) 0%, rgba(201,138,60,0) 75%),
      radial-gradient(ellipse 260px 320px at 560px 420px, var(--sienna) 0%, rgba(138,74,44,0) 75%),
      radial-gradient(ellipse 200px 200px at 650px 260px, var(--teal-splash) 0%, rgba(62,111,108,0) 70%),
      radial-gradient(ellipse 360px 260px at 200px 880px, var(--umber) 0%, rgba(107,58,34,0) 75%),
      radial-gradient(ellipse 300px 220px at 560px 820px, var(--rust) 0%, rgba(164,80,42,0) 75%),
      linear-gradient(180deg, var(--paper) 0%, var(--paper-warm) 55%, #c79a6a 100%);
  }
  .author {
    position: absolute;
    top: 22px;
    left: 0;
    width: 100%;
    text-align: center;
    font-family: "Lato", sans-serif;
    font-weight: 400;
    font-size: 29px;
    letter-spacing: 1px;
    color: var(--ink);
    text-transform: uppercase;
  }
  .title-band {
    position: absolute;
    left: 0;
    top: 1013px;
    width: 738px;
    height: 187px;
    background: var(--band-gold);
    text-align: center;
    color: var(--ink);
  }
  .title {
    margin-top: 30px;
    font-family: "Pinyon Script", cursive;
    font-weight: 400;
    font-size: 58px;
    line-height: 1.1;
  }
  .subtitle {
    margin-top: 14px;
    font-family: "Libre Baskerville", serif;
    font-size: 24px;
    line-height: 1.2;
  }
</style>
</head>
<body>
  <main class="cover">
    <div class="cover-art" role="img" aria-label="Watercolour painting of a smiling woman resting her cheek on her hand, with wild red and copper hair exploding into paint splashes"></div>
    <p class="author">Dorinda Crastley</p>
    <section class="title-band">
      <h1 class="title">Making The Bright Choice</h1>
      <p class="subtitle">Ways to build the glad days YOU seek</p>
    </section>
  </main>
</body>
</html>
```